Modern Business Card For A Digital Advertising Company

I'll be print on the Tarn Prints Velour paper http://us.tarnprints.example/products/velour/business-cards.html
Need's to be modern and use the color palette of the logo or gray scales. I think integrating the pixelation of the logo in to the card and having it wrap from one side to the other could be interesting. My company provides ad operations, web development, and number of other services to websites around the world. You can see my website at http://www.pixelharbor.example
Contact info on the card needs to have
Dana Welloby
President
p.555.318.4406
dana@pixelharbor.example
http://www.pixelharbor.example
Doesn't necessarily need to be in that order
Target Market(s)
Website owners
Industry/Entity Type
Business
Look and feel

```html
<!DOCTYPE html>
<html lang="en">
<head>
<meta charset="utf-8">
<title>Pixel Harbor – Business Card</title>
<link rel="stylesheet" href="https://fonts.googleapis.com/css2?family=Josefin+Sans:wght@300;400;600&family=Orbitron:wght@500&display=swap">
<style>
  :root {
    --brand-green: #8cc21f;
    --brand-green-deep: #79b012;
    --ink: #3a3a3a;
    --ink-soft: #6d6d6d;
    --paper: #ffffff;
    --backdrop: #ecebe8;
  }
  * { margin: 0; padding: 0; box-sizing: border-box; }
  html, body {
    width: 1200px;
    height: 623px;
    overflow: hidden;
    background: var(--backdrop);
    font-family: "Josefin Sans", Arial, sans-serif;
  }
  .card-set {
    position: relative;
    width: 1200px;
    height: 623px;
  }
  .card {
    position: absolute;
    top: 163px;
    width: 520px;
    height: 297px;
    border-radius: 3px;
    box-shadow: 0 6px 18px rgba(0,0,0,0.12);
  }

  /* Front side */
  .card--front {
    left: 50px;
    background: var(--brand-green);
    display: flex;
    flex-direction: column;
    align-items: center;
    justify-content: center;
    gap: 22px;
  }
  .brand-mark {
    display: flex;
    align-items: center;
    gap: 10px;
  }
  .brand-mark__square {
    width: 18px;
    height: 18px;
  }
  .brand-mark__name {
    font-weight: 600;
    font-size: 30px;
    letter-spacing: 2px;
    text-transform: uppercase;
    line-height: 1;
    padding-top: 4px;
  }
  .card--front .brand-mark__square { background: var(--paper); }
  .card--front .brand-mark__name { color: var(--paper); }
  .front-url {
    font-family: "Orbitron", "Josefin Sans", sans-serif;
    font-weight: 500;
    font-size: 19px;
    letter-spacing: 2px;
    color: var(--paper);
    text-transform: uppercase;
  }

  /* Back side */
  .card--back {
    left: 630px;
    background: var(--paper);
    padding: 30px 34px 32px 30px;
  }
  .card--back .brand-mark {
    position: absolute;
    top: 36px;
    left: 30px;
  }
  .card--back .brand-mark__square { background: var(--brand-green); width: 14px; height: 14px; }
  .card--back .brand-mark__name { color: var(--brand-green-deep); font-size: 22px; }
  .person {
    position: absolute;
    top: 30px;
    right: 34px;
    text-align: right;
  }
  .person__name {
    font-weight: 400;
    font-size: 26px;
    color: var(--brand-green-deep);
    line-height: 1.1;
  }
  .person__title {
    font-weight: 300;
    font-size: 16px;
    color: var(--ink-soft);
    margin-top: 2px;
  }
  .contact {
    position: absolute;
    bottom: 30px;
    font-size: 21px;
    font-weight: 400;
    color: var(--brand-green-deep);
  }
  .contact--phone { left: 30px; }
  .contact--phone .contact__label { color: var(--ink-soft); font-weight: 300; }
  .contact--email { right: 34px; font-size: 19px; }
</style>
</head>
<body>
  <main class="card-set">
    <section class="card card--front" aria-label="Card front">
      <div class="brand-mark">
        <span class="brand-mark__square"></span>
        <span class="brand-mark__name">Pixel Harbor</span>
      </div>
      <p class="front-url">www.pixelharbor.example</p>
    </section>

    <section class="card card--back" aria-label="Card back">
      <div class="brand-mark">
        <span class="brand-mark__square"></span>
        <span class="brand-mark__name">Pixel Harbor</span>
      </div>
      <div class="person">
        <p class="person__name">Dana Welloby</p>
        <p class="person__title">President</p>
      </div>
      <p class="contact contact--phone"><span class="contact__label">P.</span>555.318.4406</p>
      <p class="contact contact--email">dana@pixelharbor.example</p>
    </section>
  </main>
</body>
</html>
```